Business Card/Email Signature design

We need an new business card design for our business as well as an animated email signature design.<br/>Business Card:<br/>The business card designs need to have the following information for each director:<br/>Glen Purvis<br/>Managing Director<br/>glen@fernloxstaffing.com.au<br/>0468203917<br/>www.fernloxstaffing.com.au<br/><br/>and<br/><br/>Rosalind Tremby<br/>Director<br/>rosalind@fernloxstaffing.com.au<br/>0457390264<br/>www.fernloxstaffing.com.au<br/><br/>I will upload the Fernlox. Staffing logo designs to be used for the design. Our colours are black and white. I would like to see the designs in both coloured backgrounds.<br/><br/>For the email signature we need the same information. I also need to add a logo of our association NPLB of which i will add the logo as well. This NPLB logo does not need to be used for the business card unless it works with the design.<br/>For the animation part of the logo our company is called Fernlox. Staffing - We have a number of divisions called Fernlox. Construct, Fernlox. Property, Fernlox. Sales, Fernlox. Executive Support, Fernlox. Private PA, Fernlox. Talent and Fernlox. Coaching<br/>I would like for the email Signature to be designed so that the Fernlox. stays still but the words Construct, Property, Sales, Executive Support, Private PA, Talent and Coaching rotate through to capture attention and tell the story of what we do.<br/><br/>Any questions please don't hesitate to message me.

Industry/Entity Type

Recruiter

Contact Information for Business Card

Glen Purvis
Managing Director
glen@fernloxstaffing.com.au
0468203917
www.fernloxstaffing.com.au

Rosalind Tremby
Director
rosalind@fernloxstaffing.com.au
0457390264
www.fernloxstaffing.com.au

Font styles to use
Serif

Colors

Designer to choose colors to be used in the design.

Requirements
Must have
• The animation for the email signature as described
Should not have
• Any changes to my logo. Any colour other that black or white

```html
<!DOCTYPE html>
<html lang="en">
<head>
<meta charset="utf-8">
<title>Fernlox. Staffing – Business Card</title>
<link href="https://fonts.googleapis.com/css2?family=Lato:wght@400;900&display=swap" rel="stylesheet">
<style>
  :root {
    --ink: #08080b;
    --paper: #ffffff;
    --stage: #d9d9dc;
    --muted: #555559;
    --rule: #1a1a1a;
  }
  * { margin: 0; padding: 0; box-sizing: border-box; }
  html, body {
    width: 1200px; height: 900px; overflow: hidden;
    background: var(--stage);
    font-family: "Lato", sans-serif;
  }
  .canvas { position: relative; width: 1200px; height: 900px; }
  .card {
    position: absolute;
    width: 640px; height: 366px;
    border-radius: 22px;
    box-shadow: 0 10px 28px rgba(0,0,0,.22);
    overflow: hidden;
  }
  .card--front { left: 80px; top: 70px; background: var(--ink); color: var(--paper); }
  .card--back  { left: 480px; top: 464px; background: var(--paper); color: var(--ink); }

  .brand {
    position: absolute;
    display: flex; align-items: center; gap: 18px;
  }
  .brand__square {
    width: 78px; height: 78px;
    border: 1.5px solid currentColor;
  }
  .brand__name {
    font-weight: 900; font-size: 34px; letter-spacing: .5px; white-space: nowrap;
  }
  .card--front .brand { left: 50%; top: 50%; transform: translate(-50%, -50%); }
  .card--back .brand { left: 38px; top: 150px; gap: 14px; }
  .card--back .brand__square { width: 60px; height: 60px; border-width: 1.2px; }
  .card--back .brand__name { font-size: 24px; }

  .divider {
    position: absolute; left: 306px; top: 96px;
    width: 1.5px; height: 176px; background: var(--rule);
  }
  .contact { position: absolute; left: 336px; top: 98px; }
  .contact__name { font-weight: 900; font-size: 30px; line-height: 1.05; }
  .contact__role { font-size: 15px; color: var(--muted); margin-top: 4px; }
  .contact__list { list-style: none; margin-top: 26px; }
  .contact__item {
    display: flex; align-items: center; gap: 12px;
    font-size: 15px; color: #222; height: 26px;
  }
  .contact__item svg { width: 16px; height: 16px; flex: none; }
</style>
</head>
<body>
<div class="canvas">

  <section class="card card--front" aria-label="Card front">
    <div class="brand">
      <span class="brand__square"></span>
      <span class="brand__name">Fernlox. Staffing</span>
    </div>
  </section>

  <section class="card card--back" aria-label="Card back">
    <div class="brand">
      <span class="brand__square"></span>
      <span class="brand__name">Fernlox. Staffing</span>
    </div>

    <span class="divider"></span>

    <div class="contact">
      <h1 class="contact__name">Glen Purvis</h1>
      <p class="contact__role">Managing Director</p>
      <ul class="contact__list">
        <li class="contact__item">
          <svg viewBox="0 0 24 24" aria-hidden="true"><path fill="currentColor" d="M6.6 10.8a15.1 15.1 0 0 0 6.6 6.6l2.2-2.2a1 1 0 0 1 1-.25 11.4 11.4 0 0 0 3.6.57 1 1 0 0 1 1 1V20a1 1 0 0 1-1 1A17 17 0 0 1 3 4a1 1 0 0 1 1-1h3.5a1 1 0 0 1 1 1c0 1.25.2 2.45.57 3.57a1 1 0 0 1-.25 1z"/></svg>
          0468203917
        </li>
        <li class="contact__item">
          <svg viewBox="0 0 24 24" aria-hidden="true"><path fill="currentColor" d="M2 5h20v14H2z"/><path fill="none" stroke="#fff" stroke-width="1.6" d="M2.5 5.5 12 13l9.5-7.5"/></svg>
          glen@fernloxstaffing.com.au
        </li>
        <li class="contact__item">
          <svg viewBox="0 0 24 24" aria-hidden="true"><circle cx="12" cy="12" r="10" fill="currentColor"/><g fill="none" stroke="#fff" stroke-width="1.2"><ellipse cx="12" cy="12" rx="4.5" ry="9.5"/><path d="M2.5 12h19M4 7h16M4 17h16M12 2.5v19"/></g></svg>
          www.fernloxstaffing.com.au
        </li>
      </ul>
    </div>
  </section>

</div>
</body>
</html>
```